Set of 101 square images going from 0 to 100 coins

In my app, users accumulate points for answering questions. I need to depict how many points people accumulate (from 0 to 100) through a set of 101 square images. I thought of gold coins, but I'm open to other ideas.

```html
<!DOCTYPE html>
<html lang="en">
<head>
<meta charset="utf-8">
<title>Points Set – Gold Coin Tiles</title>
<link rel="stylesheet" href="https://fonts.googleapis.com/css2?family=Baloo+2:wght@800&display=swap">
<style>
  :root {
    --canvas-bg: #eef0f3;
    --tile-bg: #ffffff;
    --tile-shadow: rgba(0, 0, 0, 0.28);
    --label-navy: #1c3b8c;
    --gold-light: #ffe45a;
    --gold-mid: #f2c21b;
    --gold-deep: #c8920c;
    --cross-red: #e01414;
    --cross-dark: #a30c0c;
  }
  * { box-sizing: border-box; margin: 0; padding: 0; }
  html, body {
    width: 1200px;
    height: 675px;
    overflow: hidden;
    background: var(--canvas-bg);
  }
  .points-sheet {
    width: 1200px;
    height: 675px;
    display: grid;
    grid-template-columns: repeat(4, 205px);
    grid-template-rows: repeat(3, 205px);
    gap: 20px 32px;
    justify-content: center;
    align-content: center;
  }
  .points-tile {
    position: relative;
    background: var(--tile-bg);
    box-shadow: 0 1px 4px var(--tile-shadow);
  }
  .points-label {
    position: absolute;
    top: 34px;
    left: 0;
    right: 0;
    text-align: center;
    font-family: "Baloo 2", "Arial Rounded MT Bold", sans-serif;
    font-weight: 800;
    font-size: 28px;
    line-height: 1;
    color: var(--label-navy);
    white-space: nowrap;
  }
  .coin-art {
    position: absolute;
    left: 50%;
    bottom: 66px;
    width: calc(48px + var(--n) * 6px);
    height: calc(10px + var(--n) * 4px);
    transform: translateX(-50%);
    border-radius: 12px;
    background: linear-gradient(180deg, var(--gold-light) 0%, var(--gold-mid) 55%, var(--gold-deep) 100%);
  }
  .no-points-mark {
    position: absolute;
    left: 50%;
    top: 98px;
    width: 54px;
    height: 44px;
    transform: translateX(-50%);
  }
</style>
</head>
<body>
<main class="points-sheet">
  <section class="points-tile">
    <h2 class="points-label">0 point</h2>
    <svg class="no-points-mark" viewBox="0 0 58 46" aria-label="Red cross for no points">
      <path d="M8 6 L50 40 M50 6 L8 40" stroke="var(--cross-dark)" stroke-width="12" stroke-linecap="round"/>
      <path d="M8 5 L50 38 M50 5 L8 38" stroke="var(--cross-red)" stroke-width="9" stroke-linecap="round"/>
    </svg>
  </section>
  <section class="points-tile">
    <h2 class="points-label">1 point</h2>
    <div class="coin-art" style="--n:1" role="img" aria-label="One gold coin lying flat"></div>
  </section>
  <section class="points-tile">
    <h2 class="points-label">2 points</h2>
    <div class="coin-art" style="--n:2" role="img" aria-label="Two overlapping gold coins"></div>
  </section>
  <section class="points-tile">
    <h2 class="points-label">3 points</h2>
    <div class="coin-art" style="--n:3" role="img" aria-label="Three gold coins in a small pile"></div>
  </section>
  <section class="points-tile">
    <h2 class="points-label">4 points</h2>
    <div class="coin-art" style="--n:4" role="img" aria-label="Stack of four gold coins"></div>
  </section>
  <section class="points-tile">
    <h2 class="points-label">5 points</h2>
    <div class="coin-art" style="--n:5" role="img" aria-label="Five gold coins in a low pile"></div>
  </section>
  <section class="points-tile">
    <h2 class="points-label">6 points</h2>
    <div class="coin-art" style="--n:6" role="img" aria-label="Six gold coins in a pile"></div>
  </section>
  <section class="points-tile">
    <h2 class="points-label">7 points</h2>
    <div class="coin-art" style="--n:7" role="img" aria-label="Seven gold coins in two small stacks"></div>
  </section>
  <section class="points-tile">
    <h2 class="points-label">8 points</h2>
    <div class="coin-art" style="--n:8" role="img" aria-label="Eight gold coins in stacks"></div>
  </section>
  <section class="points-tile">
    <h2 class="points-label">9 points</h2>
    <div class="coin-art" style="--n:9" role="img" aria-label="Nine gold coins in stacks"></div>
  </section>
  <section class="points-tile">
    <h2 class="points-label">10 points</h2>
    <div class="coin-art" style="--n:10" role="img" aria-label="Ten gold coins in two tall stacks"></div>
  </section>
  <section class="points-tile">
    <h2 class="points-label">11 points</h2>
    <div class="coin-art" style="--n:11" role="img" aria-label="Eleven gold coins in stacks"></div>
  </section>
</main>
</body>
</html>
```